Company website for an international IT business

We require a website for our business, Korvel Solutions. The business has two primary areas: Futures, which includes two machine learning/deep learning based products and IT consultancy, which is the service we provide to other businesses.

We bridge cutting-edge research to market.

STYLING:
The site can be on single page or multi-page. This is fully open to suggestion. So long as the look and feel are consistent. Currently, we have no strong preference for colors, styles or layouts.
You can find the logo of our website in the attachment “Korvel-logo.png” and “Korvel-logo-landscape.png”.

CONTENT:
You can find the text of the website in “Website-Content.pdf”, which explains the services and products of our business. The format of the text is also open to suggestion - including breaking up the text into visually appealing sections.
We would also like to include suitable images on the website so that it does not appear to be a text-heavy page. We are happy to have placeholder images on stock image sites if needed. We are open to suggestions on placing of images

Industry/Entity Type

It Company

Coding

Coded - Design and coding required

Number of Pages Required

1 page

Colors

Designer to choose colors to be used in the design.

Requirements
Must have
• A full description of the requirement is in the attachment "Website-Content.pdf"
• The design must have HTML/CSS, and all resources relevant (images, fonts etc)
• We are
Nice to have
• We are open to suggestions on top of the requirement, please reach out and communicate.

```html
<!DOCTYPE html>
<html lang="en">
<head>
<meta charset="utf-8">
<title>Korvel Solutions</title>
<link href="https://fonts.googleapis.com/css2?family=Poppins:wght@300;400;500;600;700&display=swap" rel="stylesheet">
<style>
:root{
  --blue:#1b80c8;
  --blue-light:#3d9ad8;
  --navy:#131b29;
  --navy-deep:#0d1420;
  --ink:#222a35;
  --text:#3a414b;
  --line:#c9d6e3;
  --white:#ffffff;
}
*{margin:0;padding:0;box-sizing:border-box}
html,body{width:1200px;height:3805px;overflow:hidden;background:var(--white)}
body{font-family:'Poppins',sans-serif;color:var(--ink)}
.page{position:relative;width:1200px;height:3805px;overflow:hidden}
.abs{position:absolute}

/* top strip & nav */
.topbar{left:0;top:0;width:1200px;height:20px;background:#f1f3f5;font-size:10px;color:#7a828c}
.topbar .contact{position:absolute;left:178px;top:3px;display:flex;gap:18px}
.topbar .contact b{color:var(--blue);font-weight:500}
.topbar .search{position:absolute;left:1008px;top:4px}
.nav{left:0;top:20px;width:1200px;height:64px;background:var(--white)}
.brand{position:absolute;display:flex;align-items:center;gap:8px}
.brand .dot{width:38px;height:38px;border-radius:50%;background:var(--blue)}
.brand .name{font-weight:600;letter-spacing:1px;color:var(--navy)}
.nav .brand{left:174px;top:13px}
.nav .brand .name{font-size:16px}
.menu{position:absolute;top:23px;font-size:13px;color:#333;list-style:none}
.menu li{position:absolute;white-space:nowrap}

/* hero */
.hero{left:0;top:84px;width:1200px;height:515px;background:linear-gradient(100deg,#1d2a3d 0%,#5a6a80 18%,#2c3d56 34%,#6f7c8e 50%,#31445e 66%,#8a8f99 80%,#223247 100%)}
.hero-shade{left:0;top:84px;width:1200px;height:515px;background:linear-gradient(180deg,rgba(10,22,42,.55),rgba(10,22,42,.35) 60%,rgba(10,22,42,.6))}
.hero-frame{left:355px;top:148px;width:476px;height:232px;border:2px solid var(--blue)}
.hero-kicker{left:0;top:206px;width:1200px;text-align:center;color:#fff;font-size:22px;letter-spacing:7px;font-weight:400}
.hero-title{left:0;top:252px;width:1200px;text-align:center;color:var(--blue);font-size:92px;font-weight:700;letter-spacing:3px;line-height:1}
.hero-btn{left:515px;top:394px;width:160px;height:32px;border-radius:16px;background:var(--blue);color:#fff;font-size:14px;text-align:center;line-height:32px}
.hero-tab{left:564px;top:544px;width:72px;height:72px;border-radius:50%;background:var(--navy);z-index:3}
.hero-tab span{position:absolute;left:30px;top:18px;width:12px;height:20px;border:2px solid var(--blue);border-radius:6px}

/* about */
.circle-photo{border-radius:50%;box-shadow:0 8px 28px rgba(0,0,0,.22);border:8px solid #fff}
.about-photo{left:177px;top:685px;width:316px;height:316px;background:linear-gradient(135deg,#e6ecf2 0%,#c9b6a0 30%,#3d4c66 60%,#1f2b40 100%)}
.section-title{font-size:43px;font-weight:400;color:var(--ink);line-height:1;white-space:nowrap}
.section-title strong{color:var(--blue);font-weight:600}
.about-title{left:614px;top:718px}
.rule{height:3px;background:var(--line)}
.about-rule{left:614px;top:774px;width:300px}
.body-text{font-size:13px;line-height:28px;color:var(--text)}
.about-text{left:614px;top:806px;width:440px}
.btn-outline{height:26px;border:2px solid var(--navy);border-radius:13px;font-size:11px;text-align:center;line-height:22px;color:var(--navy)}
.about-btn{left:614px;top:1033px;width:118px}

/* video band */
.truck{left:0;top:1116px;width:1200px;height:660px;background:linear-gradient(170deg,#8b8f96 0%,#6a6a6e 25%,#4d3a38 48%,#7a2a22 60%,#3a2622 75%,#1f1715 100%)}
.truck-shade{left:0;top:1116px;width:1200px;height:660px;background:rgba(20,18,22,.25)}
.wave-top{left:0;top:1110px}
.video-line{left:0;top:1470px;width:560px;height:2px;background:rgba(255,255,255,.85)}
.play{left:559px;top:1431px;width:80px;height:80px;border-radius:50%;border:3px solid #fff}
.play::after{content:"";position:absolute;left:29px;top:22px;border-left:26px solid #fff;border-top:16px solid transparent;border-bottom:16px solid transparent}
.click-note{left:652px;top:1418px;color:#fff;font-size:15px;font-style:italic;font-weight:500}

/* product card */
.card{left:234px;top:1700px;width:756px;height:446px;background:#fff;box-shadow:0 10px 40px rgba(0,0,0,.15);text-align:center}
.card h2{margin-top:20px;font-size:34px;font-weight:400;letter-spacing:2px;line-height:1.2}
.card .rule{width:200px;margin:10px auto 16px}
.card p{width:710px;margin:0 auto;font-size:12.5px;line-height:25px;color:var(--text)}
.card .btn-outline{position:absolute;left:319px;top:394px;width:118px}

/* second product */
.street{left:0;top:2169px;width:1200px;height:546px;background:linear-gradient(100deg,#8a8377 0%,#6a645b 25%,#4a5058 45%,#2e4a66 58%,#55595c 75%,#3b3733 100%)}
.panel{left:665px;top:2233px;width:362px;height:405px;background:rgba(10,18,30,.94);color:#fff;text-align:center}
.panel h2{margin-top:30px;font-size:30px;font-weight:600;letter-spacing:2px;line-height:1.2}
.panel p{width:320px;margin:26px auto 0;font-size:12.5px;line-height:25px}
.panel .btn-light{position:absolute;left:133px;top:358px;width:96px;height:28px;background:#fff;color:var(--navy);font-size:11px;line-height:28px;border-radius:2px}

/* consultancy */
.it-title{left:172px;top:2830px}
.it-rule{left:172px;top:2888px;width:370px}
.it-text{left:172px;top:2924px;width:370px}
.it-btn{left:172px;top:3102px;width:118px}
.it-photo{left:632px;top:2778px;width:396px;height:396px;background:linear-gradient(135deg,#1e3550 0%,#3f6f96 35%,#c8b14a 55%,#e8e6e2 75%,#5d6f80 100%)}

/* footer */
.footer-wave{left:0;top:3140px}
.footer{left:0;top:3330px;width:1200px;height:425px;background:var(--navy)}
.footer .brand{left:475px;top:42px}
.footer .brand .dot{width:86px;height:86px}
.footer .brand .name{color:#fff;font-size:32px;letter-spacing:3px}
.sub-title{left:0;top:154px;width:1200px;text-align:center;color:var(--blue-light);font-size:25px;font-weight:400}
.sub-note{left:0;top:196px;width:1200px;text-align:center;color:#9aa4b2;font-size:10px}
.subscribe{left:330px;top:240px;width:538px;height:46px;border-radius:23px;overflow:hidden;display:flex;border:1px solid #56606e}
.subscribe .field{flex:1;background:var(--navy-deep);color:#8d96a3;font-size:12px;line-height:44px;padding-left:24px}
.subscribe .send{width:138px;background:#fff;color:var(--navy);font-size:15px;text-align:center;line-height:44px;font-weight:500}
.footer-contact{left:0;top:338px;width:1200px;display:flex;justify-content:center;gap:40px;color:#fff;font-size:15px}
.footer-contact span{display:flex;align-items:center;gap:8px}
.copyright{left:0;top:3755px;width:1200px;height:50px;background:var(--navy-deep);color:#cfd5dd;font-size:13px;text-align:center;line-height:50px}
</style>
</head>
<body>
<div class="page">

  <div class="abs topbar">
    <div class="contact"><span><b>Phone:</b> 555-014-2270</span><span>hello@korvelmail.net</span></div>
    <svg class="search" width="11" height="11" viewBox="0 0 11 11"><circle cx="4.5" cy="4.5" r="3.5" fill="none" stroke="#1b80c8" stroke-width="1.6"/><line x1="7" y1="7" x2="10" y2="10" stroke="#1b80c8" stroke-width="1.6"/></svg>
  </div>

  <header class="abs nav">
    <div class="brand"><span class="dot"></span><span class="name">KORVEL</span></div>
    <ul class="menu">
      <li style="left:538px">[ Home ]</li>
      <li style="left:655px">About</li>
      <li style="left:760px">Projects</li>
      <li style="left:877px">News</li>
      <li style="left:978px">Contact</li>
    </ul>
  </header>

  <section class="abs hero" role="img" aria-label="Photo of a business team in a meeting, blue toned"></section>
  <div class="abs hero-shade"></div>
  <div class="abs hero-frame"></div>
  <div class="abs hero-kicker">RESEARCH TO MARKET</div>
  <div class="abs hero-title">KORVEL</div>
  <div class="abs hero-btn">CONTACT US</div>
  <svg class="abs" style="left:142px;top:302px" width="18" height="30" viewBox="0 0 18 30"><polyline points="15,2 3,15 15,28" fill="none" stroke="#fff" stroke-width="2.5"/></svg>
  <svg class="abs" style="left:1036px;top:302px" width="18" height="30" viewBox="0 0 18 30"><polyline points="3,2 15,15 3,28" fill="none" stroke="#fff" stroke-width="2.5"/></svg>
  <div class="abs hero-tab"><span></span></div>

  <div class="abs circle-photo about-photo" role="img" aria-label="Photo of a business team joining hands in agreement"></div>
  <h2 class="abs section-title about-title"><strong>ABOUT</strong> KORVEL</h2>
  <div class="abs rule about-rule"></div>
  <p class="abs body-text about-text">Lorem ipsum dolor sit amet, consectetur adipiscing elit. Phasellus massa justo, aliquet ac ligula quis, tristique porta nibh. Curabitur consectetur blandit posuere. Nulla accumsan elementum ornare. Nulla finibus libero id viverra rhoncus. Suspendisse et feugiat nulla, at sodales mauris. Donec ante sem, sollicitudin non nunc ut, mattis mollis nisl.</p>
  <div class="abs btn-outline about-btn">READ MORE</div>

  <section class="abs truck" role="img" aria-label="Photo of a tanker truck driving on a desert road at dusk"></section>
  <div class="abs truck-shade"></div>
  <svg class="abs wave-top" width="1200" height="90" viewBox="0 0 1200 90"><path d="M0 0 H1200 V40 C1000 95 760 10 560 45 C360 80 180 20 0 55 Z" fill="#fff"/></svg>
  <div class="abs video-line"></div>
  <div class="abs play"></div>
  <div class="abs click-note">Click for more!</div>

  <article class="abs card">
    <h2>VIGIL</h2>
    <div class="rule"></div>
    <p>• The primary cause of accidents on the road are caused by human error. Of these driver distraction and fatigue are the real problem. VIGIL is a system for HGV/HMT drivers to make every journey safer – safer for the driver and safer to other road users. VIGIL uses advanced deep learning techniques to monitor driver behavior in real time inside the cabin. VIGIL can detect driver distraction (mobile phone usage, smoking, failure to focused on the road ahead) and also monitor for classic signs of fatigue. Current ADASsystems focus on external factors such as speed, distance to the vehicle ahead, keeping within road markings. By monitoring drivers for potentially dangerous driving situations VIGIL can improve safety and lower insurance costs without the need for human monitoring. This allows road freight operations to be in compliance with upcoming government regulations.</p>
    <div class="btn-outline">READ MORE</div>
  </article>

  <section class="abs street" role="img" aria-label="Photo of an old blue car parked on a weathered city street"></section>
  <article class="abs panel">
    <h2>WHEELWISE</h2>
    <p>Wheelwise is a machine learning system that tracks and analyzes live used car trading markets. It learns every aspect of a car ads, through which, it creates powerful market intelligence for all parties in the used car ecosystem: It gives inexperienced buyers independent market consensus price, depreciation and approximated running costs for cars they are interested</p>
    <div class="btn-light">READ MORE</div>
  </article>

  <h2 class="abs section-title it-title">IT <strong>CONSULTANCY</strong></h2>
  <div class="abs rule it-rule"></div>
  <p class="abs body-text it-text">The consultancy section is summarized in the "Korvel-Consultancy.pdf". The text in the deck has the spirit of the information we wish to convey. The presentation is open to suggestion and interpretation. It should also include a portfolio section, which can be filled with placeholder images and text in the design.</p>
  <div class="abs btn-outline it-btn">READ MORE</div>
  <div class="abs circle-photo it-photo" role="img" aria-label="Photo of an IT engineer working at a server rack with network cables"></div>

  <svg class="abs footer-wave" width="1200" height="200" viewBox="0 0 1200 200"><path d="M0 170 C200 210 330 110 520 120 C720 130 780 200 960 150 C1080 115 1140 20 1200 30 V200 H0 Z" fill="#131b29"/></svg>
  <footer class="abs footer">
    <div class="brand"><span class="dot"></span><span class="name">KORVEL</span></div>
    <div class="abs sub-title">Email Subscribe</div>
    <div class="abs sub-note">Subscribe now for news and updates!</div>
    <div class="abs subscribe"><div class="field">Email Address</div><div class="send">SEND</div></div>
    <div class="abs footer-contact">
      <span><svg width="16" height="16" viewBox="0 0 16 16"><path d="M3 1 L6 1 L7 5 L5 6.5 C6 9 7 10 9.5 11 L11 9 L15 10 L15 13 C15 14 14 15 13 15 C6 15 1 10 1 3 C1 2 2 1 3 1 Z" fill="none" stroke="#fff" stroke-width="1.2"/></svg>Phone: 555-019-4436</span>
      <span><svg width="18" height="14" viewBox="0 0 18 14"><rect x="1" y="1" width="16" height="12" fill="none" stroke="#fff" stroke-width="1.2"/><polyline points="1,1 9,8 17,1" fill="none" stroke="#fff" stroke-width="1.2"/></svg>Email: info@korvelmail.net</span>
    </div>
  </footer>
  <div class="abs copyright">© 2018 korvel.net All Rights Reserved.</div>

</div>
</body>
</html>
```